Business Card Design job - Tessa's Business Cards

Simple elegant feminine design - Going out on my own as a Mortgage Broker.
My thoughts are the following details on the Front, middle of the card possibly? Phone and email smaller font than my name?
Tessa Marwick
Finance Specialist
p: 0438 217 905
e: tessa@marwickfinance.com.au
Bottom of the card
residential / commercial / equipment
I would like the Font in Rose Gold maybe white or black background? or Possibly a stone grey - are you able to do a few options? I'd like them embossed
Then I had an idea as a simple logo as per the attached if you get the idea in my scribble, my initials, capital T attached to a small m that leads/follows into a circle? Thicker Font In Rose Gold, middle of the card at the back.
Very open to ideas though and what colour you think would look better with the Rose Gold.
Thanks so much for your help, I am not very creative and savvy with this stuff :-)
Industry/Entity Type
Finance
Contact Information for Business Card
Tessa Marwick
p: 0438 217 905
Look and feel
Each slider illustrates characteristics of the customer's brand and the style your logo design should communicate.

```html
<!DOCTYPE html>
<html lang="en">
<head>
<meta charset="utf-8">
<title>Tessa Marwick — Business Card</title>
<link href="https://fonts.googleapis.com/css2?family=Share+Tech+Mono&display=swap" rel="stylesheet">
<style>
  :root {
    --backdrop: #2b2a2d;
    --card-stock: #f7f5ee;
    --rose-gold: #f0ad9c;
    --rose-line: #f1b3a3;
    --stone-grey: #8e8f94;
  }
  * { margin: 0; padding: 0; box-sizing: border-box; }
  html, body {
    width: 1200px;
    height: 1200px;
    overflow: hidden;
    background: var(--backdrop);
  }
  .canvas {
    position: relative;
    width: 1200px;
    height: 1200px;
  }
  .card {
    position: absolute;
    left: 254px;
    width: 692px;
    height: 394px;
    background: var(--card-stock);
    font-family: "Share Tech Mono", monospace;
    font-style: italic;
    color: var(--rose-gold);
  }
  .card--front { top: 157px; }
  .card--back { top: 650px; }

  .contact {
    position: absolute;
    left: 0;
    right: 0;
    text-align: center;
    white-space: nowrap;
  }
  .contact__name {
    top: 82px;
    font-size: 46px;
    font-variant: small-caps;
    letter-spacing: 6px;
    line-height: 1;
  }
  .contact__rule {
    position: absolute;
    left: 165px;
    width: 388px;
    top: 130px;
    height: 2px;
    background: var(--rose-line);
  }
  .contact__title {
    top: 135px;
    font-size: 24px;
    font-variant: small-caps;
    letter-spacing: 4px;
  }
  .contact__phone {
    top: 196px;
    font-size: 25px;
    letter-spacing: 3px;
  }
  .contact__email {
    top: 233px;
    font-size: 21px;
    letter-spacing: 3px;
    text-transform: uppercase;
  }
  .services {
    position: absolute;
    left: 0;
    right: 0;
    top: 367px;
    text-align: center;
    font-size: 12px;
    letter-spacing: 6px;
    text-transform: uppercase;
    color: var(--stone-grey);
    white-space: nowrap;
  }
  .services__sep { margin: 0 14px; }

  .monogram {
    position: absolute;
    left: 0;
    top: 0;
  }
  .brand-name {
    position: absolute;
    left: 0;
    right: 0;
    top: 180px;
    text-align: center;
    font-size: 26px;
    letter-spacing: 4px;
    font-variant: small-caps;
    white-space: nowrap;
  }
</style>
</head>
<body>
  <main class="canvas">
    <section class="card card--front" aria-label="Card front">
      <h1 class="contact contact__name">Tessa Marwick</h1>
      <div class="contact__rule"></div>
      <p class="contact contact__title">Finance Specialist</p>
      <p class="contact contact__phone">0438 217 905</p>
      <p class="contact contact__email">tessa@marwickfinance.com.au</p>
      <p class="services">Residential<span class="services__sep">/</span>Commercial<span class="services__sep">/</span>Equipment</p>
    </section>

    <section class="card card--back" aria-label="Card back">
      <svg class="monogram" width="692" height="394" viewBox="0 0 692 394" aria-hidden="true">
        <circle cx="346" cy="196" r="113" fill="none" stroke="var(--rose-line)" stroke-width="2"/>
      </svg>
      <p class="brand-name">Tessa Marwick</p>
    </section>
  </main>
</body>
</html>
```